Home Care company needs letter head branding

Home care company needs a letter head which can be used for all documents the company's clients view. We provided in home care for the elderly. We would like to use our company colors (2785A7, 0A4057 and 34A74D) and should not be too large as we will be using it on more than just a letter head but all documents our clients sign / receive.
Target Market(s)
Professional business
Industry/Entity Type
Health Care
Requirements
Must have
- corporate brand colors

```html
<!DOCTYPE html>
<html lang="en">
<head>
<meta charset="utf-8">
<title>Ashgrove Care Letterhead</title>
<link rel="stylesheet" href="https://fonts.googleapis.com/css2?family=Lato:wght@400;700&family=Roboto:wght@400&display=swap">
<style>
  :root {
    --brand-blue: #2785A7;
    --brand-navy: #0A4057;
    --brand-green: #34A74D;
    --accent-lime: #9CC83B;
    --text-grey: #6f6f6f;
    --text-dark: #4a4a4a;
    --backdrop: #e9e9e9;
    --paper: #ffffff;
  }
  html, body {
    margin: 0;
    padding: 0;
    width: 1200px;
    height: 866px;
    overflow: hidden;
    background: var(--backdrop);
  }
  .letterhead {
    position: absolute;
    left: 303px;
    top: 18px;
    width: 593px;
    height: 830px;
    background: var(--paper);
    overflow: hidden;
    font-family: "Roboto", Arial, sans-serif;
    color: var(--text-grey);
  }
  .brand {
    position: absolute;
    left: 39px;
    top: 55px;
    display: flex;
    align-items: center;
    gap: 7px;
  }
  .brand-mark {
    width: 51px;
    height: 51px;
    border-radius: 50%;
    background: var(--brand-blue);
  }
  .brand-name {
    font-family: "Lato", Arial, sans-serif;
    font-weight: 700;
    font-size: 28px;
    color: var(--brand-blue);
    letter-spacing: -0.3px;
  }
  .contact {
    position: absolute;
    left: 413px;
    top: 44px;
    font-family: "Lato", Arial, sans-serif;
    font-size: 9.8px;
    line-height: 13px;
    color: var(--text-dark);
  }
  .contact-company {
    color: var(--brand-blue);
    font-weight: 700;
  }
  .contact-line {
    display: flex;
    align-items: center;
    gap: 4px;
    margin-top: 2px;
  }
  .contact-line:first-of-type { margin-top: 6px; }
  .contact-icon { width: 11px; height: 11px; }
  .recipient {
    position: absolute;
    left: 50px;
    top: 236px;
    font-size: 10.8px;
    line-height: 15.5px;
  }
  .letter-body {
    position: absolute;
    left: 50px;
    top: 329px;
    width: 492px;
    font-size: 10.6px;
    line-height: 15.4px;
    text-align: justify;
  }
  .letter-body p { margin: 0 0 15px; }
  .signature {
    position: absolute;
    left: 50px;
    top: 550px;
    width: 112px;
    height: 72px;
    background: linear-gradient(90deg, rgba(39,133,167,0.18), rgba(39,133,167,0.06));
    border-radius: 4px;
  }
  .signatory-title {
    position: absolute;
    left: 49px;
    top: 637px;
    font-size: 10.8px;
  }
  .footer-wave {
    position: absolute;
    left: 0;
    bottom: 0;
    width: 593px;
    height: 65px;
  }
  .footer-url {
    position: absolute;
    left: 423px;
    top: 799px;
    font-family: "Lato", Arial, sans-serif;
    font-size: 10.8px;
    color: #ffffff;
  }
</style>
</head>
<body>
  <main class="letterhead">
    <header>
      <div class="brand">
        <span class="brand-mark"></span>
        <span class="brand-name">Ashgrove Care</span>
      </div>
      <address class="contact" style="font-style:normal">
        <div class="contact-company">Ashgrove Care</div>
        <div>1280 Linden Hill Rd, Suite 310</div>
        <div>Riverton MD 20900</div>
        <div class="contact-line">
          <svg class="contact-icon" viewBox="0 0 12 12" aria-hidden="true">
            <circle cx="6" cy="6" r="6" fill="#2785A7"/>
            <path d="M4 3.2 L5 3 L5.6 4.6 L5 5.2 Q5.6 6.5 6.8 7 L7.4 6.4 L9 7 L8.8 8 Q6.8 8.8 4.9 7 Q3.2 5.2 4 3.2Z" fill="#fff"/>
          </svg>
          <span>(555) 014-2290</span>
        </div>
        <div class="contact-line">
          <svg class="contact-icon" viewBox="0 0 12 12" aria-hidden="true">
            <circle cx="6" cy="6" r="6" fill="#2785A7"/>
            <rect x="3" y="4" width="6" height="4.2" rx="0.5" fill="#fff"/>
            <path d="M3 4.2 L6 6.4 L9 4.2" stroke="#2785A7" stroke-width="0.7" fill="none"/>
          </svg>
          <span>info@ashgrovecare.com</span>
        </div>
      </address>
    </header>

    <div class="recipient">
      Dear Hallworth<br>
      Northfield Print Company<br>
      Department Design
    </div>

    <section class="letter-body">
      <p>Lorem ipsum dolor sit amet, consectetuer adipiscing elit. Aenean commodo ligula eget dolor. Aenean massa. Cum sociis natoque penatibus et magnis dis parturient montes, nascetur ridiculus mus. Donec quam felis, ultricies nec, pellentesque eu, pretium quis, sem. Nulla consequat massa quis enim. Donec pede justo, fringilla vel, aliquet nec, vulputate eget, arcu. In enim justo, rhoncus ut, imperdiet a, venenatis vitae, justo. Nullam dictum felis eu pede mollis pretium. Integer tincidunt. Cras dapibus. Vivamus elementum semper nisi.Nullam dictum felis eu pede mollis pretium. Integer tincidunt. Cras dapibus. Vivamus elementum semper nisi.felis eu pede mollis pretium. Integer tincidunt. Cras dapibus.</p>
      <p>Quisque rutrum. Aenean imperdiet. Etiam ultricies nisi vel augue. Curabitur ullamcorper ultricies nisi. Nam eget dui. Etiam rhoncus. Maecenas tempus, tellus eget condimentum rhoncus, sem quam semper libero, sit amet adipiscing sem neque sed ipsum.felis pede mollis pretium. I am tincidunt. Cras dapibus.</p>
    </section>

    <div class="signature" role="img" aria-label="Handwritten signature of the director"></div>
    <div class="signatory-title">Director/Executive Director</div>

    <svg class="footer-wave" viewBox="0 0 593 65" preserveAspectRatio="none" aria-hidden="true">
      <path d="M12 29 Q260 8 560 8 Q300 14 20 32 Z" fill="var(--accent-lime)"/>
      <path d="M0 26 C150 44 330 22 593 22 L593 65 L0 65 Z" fill="var(--brand-blue)"/>
    </svg>
    <div class="footer-url">www.ashgrovecare.com</div>
  </main>
</body>
</html>
```